We have a parent company, Summit Harbor Group (SHG), that has other company partners. We are looking for ways to incorporate our SHG logo with our network partners, Beacon Ledger and The Blue Gate. My initial thought is to have SHG as front of card logo, and include The Blue Gate and Beacon Ledger logos on back but I'm open to ideas. Card should include website www.summitharborgrp.example (use for reference). Keywords "Tax Services" "Real Estate" "Insurance" "Investments" "Chief Financial Officer"

Industry/Entity Type

Financial

```html
<!DOCTYPE html>
<html lang="en">
<head>
<meta charset="utf-8">
<title>Summit Harbor Group – Business Card</title>
<link rel="stylesheet" href="https://fonts.googleapis.com/css2?family=Cinzel:wght@500;600&family=Work+Sans:wght@400;500&display=swap">
<style>
  :root {
    --bg: #1e1e1f;
    --brand-blue: #1656b0;
    --brand-blue-light: #0f66ab;
    --brand-red: #e4202e;
    --ink: #3a3a3a;
    --paper: #ffffff;
  }
  * { margin: 0; padding: 0; box-sizing: border-box; }
  html, body { width: 1200px; height: 897px; overflow: hidden; background: var(--bg); }
  .stage { position: relative; width: 1200px; height: 897px; }

  .card {
    position: absolute;
    left: 354px;
    width: 486px;
    height: 278px;
    overflow: hidden;
  }
  .card--front {
    top: 161px;
    background: linear-gradient(200deg, var(--brand-blue-light) 0%, var(--brand-blue) 55%);
  }
  .card--back { top: 468px; background: var(--paper); }

  .wordmark {
    display: flex;
    align-items: center;
    gap: 10px;
    font-family: "Cinzel", serif;
    font-weight: 600;
    white-space: nowrap;
  }
  .wordmark__dot { border-radius: 50%; background: var(--brand-red); flex: none; }

  .card--front .wordmark {
    position: absolute;
    left: 0; right: 0; top: 118px;
    justify-content: center;
    color: var(--paper);
    font-size: 25px;
  }
  .card--front .wordmark__dot { width: 30px; height: 30px; }

  .card--back .wordmark {
    position: absolute;
    right: 26px; top: 38px;
    color: var(--brand-blue);
    font-size: 17px;
    gap: 7px;
  }
  .card--back .wordmark__dot { width: 20px; height: 20px; }

  .person { position: absolute; left: 0; top: 66px; }
  .person__bar { position: absolute; left: 0; top: 0; width: 9px; height: 29px; background: var(--brand-red); }
  .person__name {
    margin-left: 21px;
    font-family: "Cinzel", serif; font-weight: 600;
    font-size: 14px; color: var(--brand-red); line-height: 16px;
  }
  .person__role {
    margin-left: 21px;
    font-family: "Cinzel", serif; font-weight: 500;
    font-size: 12.5px; color: var(--brand-blue); line-height: 16px;
  }

  .contact { position: absolute; left: 20px; top: 192px; list-style: none; }
  .contact li {
    display: flex; align-items: center; gap: 8px;
    height: 18px;
    font-family: "Work Sans", sans-serif; font-size: 12px; color: var(--ink);
  }
  .contact svg { width: 10px; height: 10px; flex: none; }

  .partners {
    position: absolute; right: 24px; top: 208px;
    display: flex; align-items: center; gap: 12px;
    font-family: "Cinzel", serif; font-weight: 600; font-size: 11px;
  }
  .partners__item--ledger { color: var(--brand-blue); }
  .partners__item--gate { color: var(--brand-red); }

  .footer-band { position: absolute; left: 0; bottom: 0; width: 486px; height: 20px; }
  .footer-band__url {
    position: absolute; right: 30px; bottom: 2px;
    font-family: "Work Sans", sans-serif; font-weight: 500;
    font-size: 12.5px; color: var(--paper);
  }
</style>
</head>
<body>
<main class="stage">

  <section class="card card--front" aria-label="Card front">
    <div class="wordmark">
      <span class="wordmark__dot"></span>
      <span class="wordmark__name">Summit Harbor Group</span>
    </div>
  </section>

  <section class="card card--back" aria-label="Card back">
    <div class="person">
      <span class="person__bar"></span>
      <p class="person__name">Dana Whitlock</p>
      <p class="person__role">Founder &amp; CEO</p>
    </div>

    <div class="wordmark">
      <span class="wordmark__dot"></span>
      <span class="wordmark__name">Summit Harbor Group</span>
    </div>

    <ul class="contact">
      <li>
        <svg viewBox="0 0 10 10" aria-hidden="true"><path d="M2 0.5 L3.6 0.5 L4 3 L2.8 3.8 Q3.8 6.2 6.2 7.2 L7 6 L9.5 6.4 L9.5 8 Q9.5 9.5 8 9.5 Q1 9 0.5 2 Q0.5 0.5 2 0.5Z" fill="var(--brand-blue)"/></svg>
        555-014-2290
      </li>
      <li>
        <svg viewBox="0 0 10 10" aria-hidden="true"><rect x="0.6" y="2" width="8.8" height="6.4" fill="none" stroke="var(--brand-blue)" stroke-width="1"/><path d="M0.6 2 L5 5.6 L9.4 2" fill="none" stroke="var(--brand-blue)" stroke-width="1"/></svg>
        info@summitharborgrp.example
      </li>
      <li>
        <svg viewBox="0 0 10 10" aria-hidden="true"><path d="M9.5 0.5 L0.5 4.2 L4.6 5.4 L5.8 9.5 Z" fill="none" stroke="var(--brand-blue)" stroke-width="1" stroke-linejoin="round"/></svg>
        1200 Ridgeview Ave Lakemont, CO 80000
      </li>
    </ul>

    <div class="partners">
      <span class="partners__item partners__item--ledger">Beacon Ledger</span>
      <span class="partners__item partners__item--gate">The Blue Gate</span>
    </div>

    <svg class="footer-band" viewBox="0 0 486 20" preserveAspectRatio="none" aria-hidden="true">
      <rect x="0" y="12" width="256" height="8" fill="var(--brand-blue)"/>
      <polygon points="258,20 276,0 486,0 486,20" fill="var(--brand-red)"/>
    </svg>
    <span class="footer-band__url">www.summitharborgrp.example</span>
  </section>

</main>
</body>
</html>
```